Small Business Consulting Firm Needs Business Card Design

Need a sleek modern business card with 2 sides matching the colors of our logo. We will be placing these with a mailer we are sending out. These business cards will only ever be given to business owners. We operate helping businesses who are struggling with cash flow or finances. If the green and blue design needs to be moved to the right of "Harborline Crest Consulting" for aesthetic purposes that is ok. We will need an editable file if possible. We would like to include the reps name, email, website, and phone number. For now just use Peter Vance, pvance@harborlinecrest.com, www.harborlinecrest.com, and 833-555-0172.

```html
<!DOCTYPE html>
<html lang="en">
<head>
<meta charset="utf-8">
<title>Harborline Crest Consulting – Business Card</title>
<link rel="stylesheet" href="https://fonts.googleapis.com/css2?family=Montserrat:wght@400;500;700&family=Open+Sans:ital,wght@1,400&display=swap">
<style>
  :root {
    --page-bg: #ecebe8;
    --card-bg: #f4f4f3;
    --ink: #3a3a3c;
    --ink-soft: #444446;
    --brand-green: #5fae3c;
    --brand-green-dark: #4f9a30;
    --brand-blue: #0a72bd;
  }
  * { margin: 0; padding: 0; box-sizing: border-box; }
  html, body { width: 900px; height: 1200px; overflow: hidden; }
  body {
    background: var(--page-bg);
    font-family: "Montserrat", Arial, sans-serif;
    color: var(--ink);
    position: relative;
  }
  .card {
    position: absolute;
    background: var(--card-bg);
    box-shadow: 0 6px 18px rgba(0,0,0,0.18);
    overflow: hidden;
  }
  /* Front side */
  .card-front { left: 74px; top: 136px; width: 768px; height: 434px; }
  .rep-name {
    position: absolute; left: 41px; top: 64px;
    font-size: 28px; font-weight: 700; letter-spacing: 0.5px;
    color: var(--ink);
  }
  .rep-title {
    position: absolute; left: 42px; top: 100px;
    font-size: 17px; font-weight: 400; letter-spacing: 6px;
    color: var(--ink-soft);
  }
  .accent-dash {
    position: absolute; left: 42px; top: 182px;
    width: 28px; height: 5px; background: var(--brand-blue);
  }
  .contact-list { position: absolute; left: 41px; top: 258px; list-style: none; }
  .contact-item {
    display: flex; align-items: center; height: 30px; margin-bottom: 25px;
    font-size: 19px; font-weight: 400; letter-spacing: 0.6px; color: var(--ink);
  }
  .contact-icon {
    width: 30px; height: 30px; border-radius: 50%;
    background: var(--brand-green); margin-right: 11px;
    display: flex; align-items: center; justify-content: center; flex-shrink: 0;
  }
  .brand-block {
    position: absolute; right: 0; top: 0;
    width: 270px; height: 270px;
    background: var(--brand-green);
  }
  /* Back side */
  .card-back { left: 64px; top: 626px; width: 782px; height: 446px; }
  .brand-mark {
    position: absolute; left: 338px; top: 80px;
    width: 108px; height: 108px; background: var(--brand-blue);
  }
  .brand-name {
    position: absolute; left: 0; right: 0; top: 240px; text-align: center;
    font-size: 40px; font-weight: 400; letter-spacing: 2px; color: var(--ink);
  }
  .brand-sub {
    position: absolute; left: 0; right: 0; top: 294px; text-align: center;
    font-size: 19px; font-weight: 500; letter-spacing: 8px; color: var(--ink);
  }
  .divider {
    position: absolute; left: 61px; width: 660px; top: 375px;
    height: 2px; background: var(--brand-green);
  }
  .mission {
    position: absolute; left: 0; right: 0; top: 396px; text-align: center;
    font-family: "Open Sans", Arial, sans-serif; font-style: italic;
    font-size: 17px; color: var(--ink-soft);
  }
</style>
</head>
<body>

<section class="card card-front">
  <div class="rep-name">PETER VANCE</div>
  <div class="rep-title">DIRECTOR</div>
  <div class="accent-dash"></div>
  <ul class="contact-list">
    <li class="contact-item">
      <span class="contact-icon">
        <svg width="16" height="16" viewBox="0 0 24 24" aria-hidden="true"><path fill="#fff" d="M6.6 10.8a15 15 0 0 0 6.6 6.6l2.2-2.2c.3-.3.7-.4 1-.2 1.1.4 2.3.6 3.6.6.6 0 1 .4 1 1V20c0 .6-.4 1-1 1A17 17 0 0 1 3 4c0-.6.4-1 1-1h3.5c.6 0 1 .4 1 1 0 1.3.2 2.5.6 3.6.1.3 0 .7-.2 1z"/></svg>
      </span>833-555-0172
    </li>
    <li class="contact-item">
      <span class="contact-icon">
        <svg width="16" height="16" viewBox="0 0 24 24" aria-hidden="true"><rect x="3" y="6" width="18" height="12" rx="1.5" fill="#fff"/><path d="M3.5 6.5 12 13l8.5-6.5" fill="none" stroke="#5fae3c" stroke-width="1.6"/></svg>
      </span>PVANCE@HARBORLINECREST.COM
    </li>
    <li class="contact-item">
      <span class="contact-icon">
        <svg width="18" height="18" viewBox="0 0 24 24" aria-hidden="true" fill="none" stroke="#fff" stroke-width="1.6"><circle cx="12" cy="12" r="8.5"/><ellipse cx="12" cy="12" rx="3.8" ry="8.5"/><path d="M3.5 12h17M5 7.5h14M5 16.5h14"/></svg>
      </span>WWW.HARBORLINECREST.COM
    </li>
  </ul>
  <div class="brand-block"></div>
</section>

<section class="card card-back">
  <div class="brand-mark"></div>
  <div class="brand-name">HARBORLINE CREST</div>
  <div class="brand-sub">CONSULTING</div>
  <div class="divider"></div>
  <p class="mission">Our mission is to help business owners to grow their business.</p>
</section>

</body>
</html>
```